Poster for denture clinic rebrand

We need a poster for our denture clinic that will be a tool to market us

We want to use this poster as a marketing tool. We want our contact information on it, our website www. brelvanoth.co.nz, our phone number 0800 47 3815 and email info@brelvanoth.co.nz
The poster will convey a message of our "Vantrel system" which guarantees a lifetime of care for your dentures. Including replacement dentures, relines, repairs.

The size of the poster will be A1 or 594mm x 840mm

We want the poster to be relatively simple and colourful and not too busy. We are an upmarket clinic so this must be reflected in the poster.
We have attached some files so that the poster can be in line with our logo, colours etc.

Target Market(s)

Aged 45+

Industry/Entity Type

Dental Clinic

Font styles to use
Serif
Sans Serif

Colors
f37122
0355a3

Requirements
Must have
• - Our colours
• - Eye catching
• - Contact info
• - Bold fonts
Should not have
• - Should not be too busy or crowded

```html
<!DOCTYPE html>
<html lang="en">
<head>
<meta charset="utf-8">
<title>Vantrel system – Brelvanoth</title>
<link rel="stylesheet" href="https://fonts.googleapis.com/css2?family=Libre+Baskerville:wght@400;700&family=Quicksand:wght@500;600;700&display=swap">
<style>
  :root {
    --brand-blue: #3378b8;
    --deep-blue: #0355a3;
    --brand-orange: #f37122;
    --tag-grey: #7a7f85;
    --white: #ffffff;
  }
  html, body {
    margin: 0;
    padding: 0;
    overflow: hidden;
    background: var(--white);
  }
  .poster {
    position: relative;
    width: 849px;
    height: 1200px;
    overflow: hidden;
    background: var(--white);
    font-family: "Quicksand", sans-serif;
  }
  .band {
    position: absolute;
    left: 0;
    width: 849px;
  }
  .band--top { top: 0; height: 100px; }
  .band--bottom { bottom: 0; height: 100px; }

  .brand {
    position: absolute;
    top: 78px;
    left: 440px;
    width: 345px;
    text-align: center;
  }
  .brand__square {
    display: block;
    width: 68px;
    height: 66px;
    margin: 0 auto 6px 138px;
    background: var(--brand-blue);
  }
  .brand__name {
    margin: 0;
    font-family: "Quicksand", sans-serif;
    font-weight: 700;
    font-size: 35px;
    line-height: 38px;
    letter-spacing: 1px;
    color: var(--deep-blue);
  }
  .brand__tagline {
    margin: 2px 0 0;
    font-weight: 500;
    font-size: 14.5px;
    letter-spacing: 3.4px;
    color: var(--tag-grey);
  }

  .headline {
    position: absolute;
    top: 362px;
    left: 48px;
    margin: 0;
    font-family: "Libre Baskerville", serif;
    font-weight: 400;
    font-size: 66px;
    line-height: 80px;
    letter-spacing: 1px;
    color: var(--brand-blue);
    white-space: nowrap;
  }

  .promise {
    font-family: "Libre Baskerville", serif;
    font-weight: 700;
    color: var(--brand-blue);
    margin: 0;
  }
  .promise span { position: absolute; white-space: nowrap; }
  .promise__a { top: 484px; left: 45px; font-size: 21px; }
  .promise__b { top: 517px; left: 230px; font-size: 21px; }
  .promise__c { top: 558px; left: 72px; font-size: 21px; }
  .promise__c b { font-size: 32px; }
  .promise__d { top: 604px; left: 158px; font-size: 40px; }

  .portrait {
    position: absolute;
    left: 370px;
    top: 615px;
    width: 479px;
    height: 540px;
    background:
      radial-gradient(ellipse 32% 38% at 58% 40%, #e9b79c 0%, #dba083 55%, rgba(219,160,131,0) 100%),
      radial-gradient(ellipse 55% 60% at 60% 45%, #3b2a22 0%, #4a3429 60%, rgba(74,52,41,0) 100%),
      radial-gradient(ellipse 50% 22% at 45% 98%, #2f5c8c 0%, rgba(47,92,140,0) 100%);
  }

  .address {
    position: absolute;
    left: 80px;
    top: 1186px;
    margin: 0;
    font-size: 13px;
    font-weight: 500;
    color: var(--white);
    white-space: nowrap;
  }
  .contact {
    position: absolute;
    right: 68px;
    top: 1112px;
    margin: 0;
    font-style: normal;
    text-align: right;
    font-size: 13px;
    line-height: 16px;
    font-weight: 500;
    color: var(--white);
  }
  .contact b { font-weight: 700; }
</style>
</head>
<body>
<main class="poster">
  <svg class="band band--top" viewBox="0 0 849 100" aria-hidden="true">
    <path d="M0 0 H849 V48 H375 C345 48 335 92 300 92 H0 Z" fill="var(--brand-blue)"/>
    <path d="M375 55 H849 V66 H388 C378 66 370 70 364 76 C366 64 370 55 375 55 Z" fill="var(--brand-orange)"/>
  </svg>

  <header class="brand">
    <span class="brand__square" aria-hidden="true"></span>
    <p class="brand__name">BRELVANOTH</p>
    <p class="brand__tagline">THE DENTURE EXPERTS</p>
  </header>

  <h1 class="headline">Vantrel system</h1>

  <p class="promise">
    <span class="promise__a">guarantees a</span>
    <span class="promise__b">lifetime</span>
    <span class="promise__c">of <b>care</b> for</span>
    <span class="promise__d">your dentures...</span>
  </p>

  <div class="portrait" role="img" aria-label="Photo of a smiling woman with dark hair looking upward"></div>

  <svg class="band band--bottom" viewBox="0 0 849 100" aria-hidden="true">
    <path d="M0 34 H500 C490 38 486 42 482 46 H0 Z" fill="var(--brand-orange)"/>
    <path d="M0 48 H490 C510 48 512 8 545 8 H849 V100 H0 Z" fill="var(--brand-blue)"/>
  </svg>

  <p class="address">148 Kowhai Rd Ranui Auckland 0612</p>
  <address class="contact">
    <b>P:</b> 0800 47 3815<br>
    <b>C:</b> 09 512 7740<br>
    info@brelvanoth.co.nz<br>
    www.brelvanoth.co.nz
  </address>
</main>
</body>
</html>
```